Case Study - template Visual Design

We need to convert our current case study document into something more cosmetically pleasing and easy to read. (primary goal). We also want to make sure the design is reusable for future case studies as well.
Current case study content is uploaded for reference.
Company is Plonex.ai
Target Market(s)
Mid to large Enterprise
Industry/Entity Type
Iot
Font styles to use
Sans Serif
Colors
Designer to choose colors to be used in the design.

```html
<!DOCTYPE html>
<html lang="en">
<head>
<meta charset="utf-8">
<title>Plonex.ai — Case Study Cover</title>
<link href="https://fonts.googleapis.com/css2?family=Righteous&display=swap" rel="stylesheet">
<style>
  :root {
    --backdrop: #e3e3e3;
    --paper: #fbfbfb;
    --paper-edge: #f1f1f1;
    --ink: #141414;
    --mint: #93cbb2;
    --teal: #80a8a8;
    --steel: #8aa0c2;
    --lavender: #9d93c9;
    --title: #ffffff;
  }
  * { margin: 0; padding: 0; box-sizing: border-box; }
  html, body {
    width: 1200px;
    height: 790px;
    overflow: hidden;
    background: var(--backdrop);
  }
  .canvas {
    position: relative;
    width: 1200px;
    height: 790px;
  }
  .cover {
    position: absolute;
    left: 338px;
    top: 25px;
    width: 523px;
    height: 740px;
    background: linear-gradient(160deg, var(--paper) 0%, var(--paper-edge) 100%);
    box-shadow: 0 6px 18px rgba(0,0,0,0.12);
    overflow: hidden;
  }
  .cover__band {
    position: absolute;
    left: 0;
    top: 290px;
    width: 100%;
    height: 360px;
    background: linear-gradient(90deg, var(--mint) 0%, var(--teal) 35%, var(--steel) 70%, var(--lavender) 100%);
  }
  .brand {
    position: absolute;
    left: 44px;
    top: 50px;
    display: flex;
    align-items: center;
    gap: 10px;
    font-family: "Righteous", sans-serif;
    font-size: 22px;
    color: var(--ink);
  }
  .brand__mark {
    width: 16px;
    height: 16px;
    background: var(--lavender);
  }
  .cover__title {
    position: absolute;
    left: 92px;
    top: 530px;
    font-family: "Righteous", sans-serif;
    font-weight: 400;
    font-size: 27px;
    line-height: 1.2;
    letter-spacing: 0.5px;
    color: var(--title);
  }
</style>
</head>
<body>
  <main class="canvas">
    <article class="cover">
      <div class="cover__band" role="img" aria-label="Decorative mint-to-lavender flowing wave graphic with fine dot texture"></div>

      <div class="brand">
        <span class="brand__mark"></span>
        <span class="brand__name">Plonex</span>
      </div>

      <h1 class="cover__title">Predictive Maintenance<br>With Machine Learning</h1>
    </article>
  </main>
</body>
</html>
```